Door Hanger Design for Electricians Serving Homes

I would like our logo incorporated into the door hanger. We would like a place for a tear off section on the bottom of the hanger with our contact information: K&T Electric - (555) 318-6470 - www.kandtelectric.example - info@kandtelectric.example.
Door Hanger Script
Front Side of the Door Hanger:
[Company Logo]
Need a Reliable Electrician?
Your Local Electrical Expert is Just Around the Corner!
• Quick Response Times
• Affordable Rates
• Quality Workmanship
• Fully Licensed & Insured
• Special Offer:
• 10% OFF Your First Service Call!
Back Side of the Door Hanger:
Don't Let Electrical Issues Keep You in the Dark!
From flickering lights to complete system upgrades, we've got all your
residential electrical needs covered. Our services include:
• Electrical Repairs & Troubleshooting
• Lighting Installation & Upgrades
• Safety Inspections & Code Compliance
• Energy-Efficient Solutions
• 24/7 Emergency Services
• Why Choose Us?
• Friendly, Local Service
• Over 30 Years of Experience
• Satisfaction Guaranteed
• Upfront Pricing
Call Us Today: [Your Phone Number]
Visit Our Website: [Your Website]
Book Your Appointment Now and Claim Your 10% Discount!
Offer valid for new customers on the first visit only. Mention this door hanger when
booking.
[Your Company Name and Contact Information]
Follow Us on Social Media for More Tips and Special Offers!
[Icons for social media platforms: Chatterbook, Snapwave, Peeper, etc.]
Design Tips:
Use bold, clear fonts for easy reading.
Incorporate your brand colors and logo for instant recognition.
Include a clear call to action (CTA) on both sides.
Add a tear-off section at the bottom with your contact information for
convenience.
Use high-quality images or graphics related to electrical work to catch
the eye.
This door hanger design and copy aim to attract residential clients by
highlighting the benefits of your electrical services, special offers, and
how they can easily get in touch with you for their electrical needs.
The door knocker template will have three of the same design on front and three of the same design on the back. This template is from the print shop.

```html
<!DOCTYPE html>
<html lang="en">
<head>
<meta charset="utf-8">
<title>K&amp;T Electric Door Hangers</title>
<link href="https://fonts.googleapis.com/css2?family=Montserrat:wght@800;900&family=Roboto+Condensed:wght@400;500;700&family=Roboto:wght@300;400;700&display=swap" rel="stylesheet">
<style>
:root{
  --red:#f2141b;
  --red-deep:#d10d12;
  --dark:#1d1d1f;
  --charcoal:#3a3a3c;
  --grey:#c9c9cb;
  --stage:#e2e2e2;
  --white:#ffffff;
}
*{margin:0;padding:0;box-sizing:border-box}
html,body{width:1200px;height:1200px;overflow:hidden;background:var(--stage)}
.stage{position:relative;width:1200px;height:1200px}
.hanger{position:absolute;top:73px;width:460px;height:1057px;background:var(--white);overflow:hidden;box-shadow:8px 12px 22px rgba(0,0,0,.28);font-family:"Roboto Condensed",sans-serif;color:var(--white)}
.hanger--front{left:110px}
.hanger--back{left:630px}
.abs{position:absolute}
.photo{position:absolute}
.hole{position:absolute;left:168px;top:78px;width:124px;height:124px;border-radius:50%;background:var(--stage);z-index:5}
.heavy{font-family:"Montserrat",sans-serif;font-weight:900;line-height:1}
.thin{font-family:"Roboto",sans-serif;font-weight:300;line-height:1}

/* front */
.brand{position:absolute;left:150px;top:440px;width:170px;text-align:center;font-family:"Roboto Condensed",sans-serif;font-weight:700;font-size:30px;color:var(--dark);line-height:1}
.headline-band{position:absolute;left:0;top:519px;width:460px;height:119px;background:var(--red)}
.kicker{position:absolute;top:548px;width:460px;text-align:center;font-size:26px;color:var(--white);z-index:3}
.main-title{position:absolute;left:38px;top:566px;font-size:45px;color:var(--white);z-index:3}
.pill{position:absolute;left:52px;top:623px;width:356px;height:30px;border-radius:15px;background:#ededed;color:var(--dark);font-size:15px;text-align:center;line-height:30px;z-index:4;white-space:nowrap}
.benefits{position:absolute;left:0;top:638px;width:460px;height:272px;background:var(--dark);z-index:1}
.benefit{position:absolute;top:40px;width:96px;text-align:center}
.benefit-icon{width:58px;height:58px;margin:0 auto;border-radius:50%;border:2px dotted var(--red);display:flex;align-items:center;justify-content:center}
.benefit-label{margin-top:12px;font-weight:700;font-size:17px;line-height:1.02}
.offer-box{position:absolute;left:23px;top:843px;width:416px;height:146px;border-radius:12px;background:linear-gradient(120deg,#d6d6d8,#ffffff 55%,#d0d0d2);border:2px dotted var(--red);z-index:2}
.offer-tab{position:absolute;left:125px;top:834px;width:208px;height:28px;background:var(--red);clip-path:polygon(6% 0,94% 0,100% 50%,94% 100%,6% 100%,0 50%);color:var(--white);text-align:center;font-family:"Roboto",sans-serif;font-weight:300;font-size:21px;line-height:28px;z-index:3}
.big-pct{position:absolute;color:var(--red);font-size:108px;letter-spacing:-3px;z-index:3}
.off{position:absolute;color:var(--red);font-size:40px;z-index:3}
.first-call{position:absolute;left:272px;top:918px;color:var(--dark);font-family:"Roboto",sans-serif;font-weight:400;font-size:20px;line-height:1.05;z-index:3}
.footer{position:absolute;left:0;top:989px;width:460px;height:68px;z-index:4}
.call{position:absolute;left:48px;top:14px;color:var(--white)}
.call small{display:block;font-family:"Roboto",sans-serif;font-weight:300;font-size:14px}
.call strong{display:block;font-family:"Roboto",sans-serif;font-weight:700;font-size:21px;letter-spacing:.3px}
.web{position:absolute;left:278px;top:19px;color:var(--white);font-family:"Roboto",sans-serif;font-weight:300;font-size:13.5px;line-height:1.15}
.web b{font-weight:700}
.divider{position:absolute;top:15px;width:1px;height:38px;background:rgba(255,255,255,.7)}

/* back */
.back-title{position:absolute;left:31px;color:var(--white);z-index:3}
.intro{position:absolute;left:31px;top:468px;width:250px;font-size:16.5px;line-height:1.22;color:var(--white);z-index:3}
.services{position:absolute;left:0;top:566px;width:460px;height:297px;background:var(--dark)}
.service{position:absolute;font-weight:700;font-size:17px;line-height:1.2;padding-left:16px}
.bolt{position:absolute;left:0;top:2px;width:11px;height:16px}
.why-box{position:absolute;left:41px;top:735px;width:379px;height:126px;background:var(--white);border:2px dotted var(--red);border-radius:12px;z-index:2}
.why-tab{position:absolute;left:126px;top:720px;width:210px;height:30px;background:var(--dark);clip-path:polygon(0 0,100% 0,94% 100%,6% 100%);text-align:center;color:var(--white);font-family:"Roboto",sans-serif;font-weight:300;font-size:20px;line-height:30px;z-index:4}
.why-item{position:absolute;left:218px;color:var(--dark);font-size:15px;padding-left:14px;z-index:3}
.book{position:absolute;left:72px;top:861px;width:317px;height:28px;background:var(--charcoal);border-radius:0 0 12px 12px;text-align:center;font-family:"Roboto",sans-serif;font-weight:400;font-size:11.5px;line-height:28px;letter-spacing:.2px;z-index:3}
.back-pct{font-size:96px}
.back-off{font-size:40px}
.fine{position:absolute;left:246px;top:932px;color:var(--charcoal);font-family:"Roboto",sans-serif;font-style:italic;font-size:7.6px;line-height:1.3;z-index:3}
.social{position:absolute;left:258px;top:961px;width:202px;height:25px;background:var(--red);clip-path:polygon(5% 0,100% 0,100% 100%,0 100%);z-index:3}
.social p{position:absolute;left:18px;top:5px;font-family:"Roboto",sans-serif;font-weight:700;font-size:5.6px;line-height:1.25}
.social .dots{position:absolute;left:122px;top:7px;display:flex;gap:6px;padding-left:8px;border-left:1px solid rgba(255,255,255,.7)}
.social .dots span{width:11px;height:11px;border-radius:50%;background:var(--white)}
</style>
</head>
<body>
<main class="stage">

  <!-- FRONT -->
  <section class="hanger hanger--front">
    <div class="photo" role="img" aria-label="Electrician in hard hat and safety glasses working at a breaker panel, with a red-tinted wiring panel on the left" style="left:0;top:0;width:460px;height:519px;background:linear-gradient(100deg,#e0262c 0%,#e94c50 38%,#b9b9bb 52%,#6e6e72 78%,#2b2b2e 100%)"></div>
    <svg class="abs" style="left:0;top:0" width="460" height="519" viewBox="0 0 460 519">
      <polygon points="0,0 78,0 0,90" fill="#ffffff"/>
      <polygon points="0,143 102,143 32,430 0,480" fill="#ffffff"/>
      <polygon points="140,8 285,8 290,30 190,190 0,519 0,460 165,160" fill="none" stroke="#ffffff" stroke-width="2" opacity=".8"/>
      <polygon points="0,519 0,460 195,160 250,160 180,330 460,330 460,519" fill="#c4c4c6" opacity=".55"/>
      <polygon points="330,519 460,330 460,519" fill="#2a2a2c"/>
    </svg>
    <div class="hole"></div>
    <div class="brand">K&amp;T Electric</div>

    <div class="headline-band"></div>
    <div class="kicker thin">NEED A RELIABLE</div>
    <div class="main-title heavy">ELECTRICIAN?</div>

    <div class="benefits">
      <div class="benefit" style="left:27px">
        <div class="benefit-icon"><svg width="30" height="30" viewBox="0 0 30 30" fill="none" stroke="#fff" stroke-width="1.6"><circle cx="9" cy="8" r="3"/><circle cx="15" cy="6" r="3"/><circle cx="21" cy="8" r="3"/><path d="M4 18c1-4 9-4 10 0M16 18c1-4 9-4 10 0M3 24l8-3 8 1 8-4"/></svg></div>
        <div class="benefit-label">Quick<br>Response<br>Times</div>
      </div>
      <div class="benefit" style="left:122px">
        <div class="benefit-icon"><svg width="30" height="30" viewBox="0 0 30 30" fill="none" stroke="#fff" stroke-width="1.6"><circle cx="19" cy="9" r="7"/><path d="M19 5v8M17 7h3a1.5 1.5 0 010 3h-2a1.5 1.5 0 000 3h3"/><path d="M4 16h4v11H4zM8 17l5-3 2 2v3h6v6H8"/></svg></div>
        <div class="benefit-label">Affordable<br>Rates</div>
      </div>
      <div class="benefit" style="left:217px">
        <div class="benefit-icon"><svg width="30" height="30" viewBox="0 0 30 30" fill="none" stroke="#fff" stroke-width="1.6"><path d="M9 11a6 6 0 0112 0H9zM7 11h16"/><circle cx="15" cy="15" r="4"/><path d="M6 28c0-6 4-8 9-8s9 2 9 8z"/></svg></div>
        <div class="benefit-label">Quality<br>Workman-<br>ship</div>
      </div>
      <div class="benefit" style="left:313px">
        <div class="benefit-icon"><svg width="30" height="30" viewBox="0 0 30 30" fill="none" stroke="#fff" stroke-width="1.6"><path d="M9 4h14v22H9z"/><path d="M12 9h8M12 13h8"/><circle cx="20" cy="20" r="4"/><path d="M18 20l1.5 1.5 3-3"/><path d="M4 26h8"/></svg></div>
        <div class="benefit-label">Fully<br>Licensed<br>&amp; Insured</div>
      </div>
    </div>
    <div class="pill">Your Local Electrical Expert is Just Around the Corner!</div>

    <div class="offer-box"></div>
    <div class="offer-tab">SPECIAL OFFER:</div>
    <div class="big-pct heavy" style="left:52px;top:868px">10%</div>
    <div class="off heavy" style="left:272px;top:876px">OFF</div>
    <div class="first-call">YOUR FIRST<br>SERVICE CALL!</div>

    <div class="footer">
      <svg class="abs" style="left:0;top:0" width="460" height="68" viewBox="0 0 460 68">
        <rect width="460" height="68" fill="#3a3a3c"/>
        <polygon points="0,0 222,0 215,68 0,68" fill="#f2141b"/>
        <polygon points="230,-80 208,0 240,-2 212,68 252,68 282,-4 252,-4 262,-80" fill="#ffffff"/>
        <path d="M26 23c3-3 5-2 6 0l-2 4c1 4 3 7 6 9l3-2c3 1 4 3 1 6-6 2-16-8-14-17z" fill="#fff"/>
        <circle cx="258" cy="37" r="8" fill="#f2141b"/>
      </svg>
      <div class="divider" style="left:43px"></div>
      <div class="call"><small>Call Us Today:</small><strong>555-318-6470</strong></div>
      <div class="divider" style="left:272px"></div>
      <div class="web">Visit Our Website<br>www.<b>kandtelectric</b>.example</div>
    </div>
  </section>

  <!-- BACK -->
  <section class="hanger hanger--back">
    <div class="photo" role="img" aria-label="Red-tinted electrical panel wiring on the left and an electrician with tablet checking a breaker panel on the right" style="left:0;top:0;width:460px;height:566px;background:linear-gradient(100deg,#e0262c 0%,#e7393e 45%,#c9c9cb 60%,#8e8e92 85%,#2b2b2e 100%)"></div>
    <svg class="abs" style="left:0;top:0" width="460" height="640" viewBox="0 0 460 640">
      <polygon points="360,0 405,0 290,225 330,225 270,290 160,290" fill="#ffffff" opacity=".85"/>
      <polygon points="405,0 460,0 460,140 375,140" fill="#1d1d1f"/>
      <polygon points="0,280 335,280 265,566 0,566" fill="#f2141b"/>
      <polygon points="335,280 460,250 460,566 265,566" fill="#1d1d1f" opacity=".85"/>
      <polygon points="460,260 460,280 280,566 262,566" fill="#ffffff"/>
      <polygon points="300,470 330,470 270,566 255,566" fill="#9fa3b0"/>
    </svg>
    <div class="hole"></div>
    <div class="photo" role="img" aria-label="Close-up of hands testing an outlet with a multimeter" style="left:264px;top:339px;width:162px;height:162px;border-radius:50%;border:3px solid #fff;background:radial-gradient(circle at 50% 45%,#d7c26a,#8d8a80 55%,#5b5b5e);z-index:2"></div>

    <div class="back-title thin" style="top:290px;font-size:25px">DON'T LET</div>
    <div class="back-title heavy" style="top:312px;font-size:39px">ELECTRICAL</div>
    <div class="back-title heavy" style="top:350px;font-size:56px">ISSUES</div>
    <div class="back-title heavy" style="top:402px;font-size:32px">KEEP YOU IN</div>
    <div class="back-title heavy" style="top:432px;font-size:32px">THE DARK!</div>
    <div class="intro">From flickering lights to complete system upgrades, we've got all your residential electrical needs covered. Our services include:</div>

    <div class="services">
      <div class="service" style="left:31px;top:13px"><svg class="bolt" viewBox="0 0 11 16"><polygon points="7,0 1,9 5,9 3,16 10,6 6,6 8,0" fill="#f2141b"/></svg>Electrical<br>Repairs &amp;<br>Troubleshooting</div>
      <div class="service" style="left:178px;top:13px"><svg class="bolt" viewBox="0 0 11 16"><polygon points="7,0 1,9 5,9 3,16 10,6 6,6 8,0" fill="#f2141b"/></svg>Lighting<br>Installation<br>&amp; Upgrades</div>
      <div class="service" style="left:289px;top:13px"><svg class="bolt" viewBox="0 0 11 16"><polygon points="7,0 1,9 5,9 3,16 10,6 6,6 8,0" fill="#f2141b"/></svg>Safety Inspections<br>&amp; Code Compliance</div>
      <div class="service" style="left:31px;top:92px"><svg class="bolt" viewBox="0 0 11 16"><polygon points="7,0 1,9 5,9 3,16 10,6 6,6 8,0" fill="#f2141b"/></svg>Energy-Efficient<br>Solutions</div>
      <div class="service" style="left:178px;top:90px"><svg class="bolt" viewBox="0 0 11 16"><polygon points="7,0 1,9 5,9 3,16 10,6 6,6 8,0" fill="#f2141b"/></svg>24/7 Emergency<br>Services</div>
    </div>
    <div class="abs" style="left:0;top:790px;width:460px;height:200px;background:#fff"></div>

    <div class="why-box"></div>
    <div class="why-tab">WHY CHOOSE US?</div>
    <div class="photo" role="img" aria-label="Cartoon electrician mascot in cap and overalls holding a lightning bolt" style="left:55px;top:752px;width:125px;height:106px;border-radius:10px;background:linear-gradient(160deg,#dfe4ee,#c33a3a 60%,#3b5fa6);z-index:3"></div>
    <div class="why-item" style="top:752px"><svg class="bolt" viewBox="0 0 11 16" style="width:10px;height:15px"><polygon points="7,0 1,9 5,9 3,16 10,6 6,6 8,0" fill="#f2141b"/></svg>Friendly, Local Service</div>
    <div class="why-item" style="top:778px"><svg class="bolt" viewBox="0 0 11 16" style="width:10px;height:15px"><polygon points="7,0 1,9 5,9 3,16 10,6 6,6 8,0" fill="#f2141b"/></svg>Over 30 Years of Experience</div>
    <div class="why-item" style="top:804px"><svg class="bolt" viewBox="0 0 11 16" style="width:10px;height:15px"><polygon points="7,0 1,9 5,9 3,16 10,6 6,6 8,0" fill="#f2141b"/></svg>Satisfaction Guaranteed</div>
    <div class="why-item" style="top:830px"><svg class="bolt" viewBox="0 0 11 16" style="width:10px;height:15px"><polygon points="7,0 1,9 5,9 3,16 10,6 6,6 8,0" fill="#f2141b"/></svg>Upfront Pricing</div>
    <div class="book">BOOK YOUR APPOINTMENT NOW AND CLAIM YOUR</div>

    <div class="big-pct back-pct heavy" style="left:38px;top:884px">10%</div>
    <div class="off back-off heavy" style="left:244px;top:892px">OFF</div>
    <div class="fine">Offer valid for new customers on the first visit only.<br>Mention this door hanger when booking.</div>
    <div class="social">
      <p>Follow Us on Social Media<br>for More Tips and Special Offers!</p>
      <div class="dots" aria-label="Chatterbook, Snapwave, Linkpost and Peeper"><span></span><span></span><span></span><span></span></div>
    </div>

    <div class="footer">
      <svg class="abs" style="left:0;top:0" width="460" height="68" viewBox="0 0 460 68">
        <rect width="460" height="68" fill="#3a3a3c"/>
        <polygon points="0,0 222,0 215,68 0,68" fill="#f2141b"/>
        <polygon points="230,-80 208,0 240,-2 212,68 252,68 282,-4 252,-4 262,-80" fill="#c9c9cb"/>
        <path d="M26 23c3-3 5-2 6 0l-2 4c1 4 3 7 6 9l3-2c3 1 4 3 1 6-6 2-16-8-14-17z" fill="#fff"/>
        <circle cx="258" cy="37" r="8" fill="#f2141b"/>
      </svg>
      <div class="divider" style="left:43px"></div>
      <div class="call"><small>Call Us Today:</small><strong>555-318-6470</strong></div>
      <div class="divider" style="left:272px"></div>
      <div class="web">Visit Our Website<br>www.<b>kandtelectric</b>.example</div>
    </div>
  </section>

</main>
</body>
</html>
```